Simple but strong message business card.

I will be using this to communicate a message about how we are different from our main competitor. I will be giving these out at a trade show. It needs to have our logo and then communicate that we do not charge PCI Fees. Our competitor charges junk fees at an exorbitant amount and our target audience is aware of it and tired of the BS.

Target Market(s)

Attendees of a trade show. General managers of the ridgeline growers union. www.fieldhaven.example

Contact Information for Business Card

Font styles to use
Sans Serif

Colors

Designer to choose colors to be used in the design.

Requirements
Must have
• Our logo. and the message of No PCI Fees
• contact email - tmorvell@brixtender.example
• contact name - Dana Morvell
• contact phone - 555-214-3980

```html
<!DOCTYPE html>
<html lang="en">
<head>
<meta charset="utf-8">
<title>Brixtender Payments — Business Card</title>
<link rel="stylesheet" href="https://fonts.googleapis.com/css2?family=Arimo:wght@400;700&display=swap">
<style>
  :root {
    --stage: #262626;
    --card-dark: #1b1b1b;
    --card-light: #2a2a2a;
    --green: #6db33f;
    --grey: #8c8c8c;
    --glow: rgba(109, 179, 63, 0.35);
  }
  * { box-sizing: border-box; margin: 0; padding: 0; }
  html, body {
    width: 1200px; height: 900px; overflow: hidden;
    background: var(--stage);
    font-family: "Arimo", Arial, sans-serif;
  }
  .card {
    position: absolute; left: 292px; width: 616px; height: 342px;
    border-radius: 22px; overflow: hidden;
    background: linear-gradient(120deg, var(--card-light) 0%, var(--card-dark) 70%);
    box-shadow: 0 6px 16px rgba(0,0,0,0.45);
  }
  .card--front { top: 88px; }
  .card--back { top: 470px; }
  .texture {
    position: absolute; right: 0; top: 0; width: 260px; height: 100%;
    background:
      radial-gradient(ellipse 60% 70% at 85% 45%, var(--glow) 0%, rgba(109,179,63,0.08) 55%, transparent 80%),
      linear-gradient(90deg, transparent 0%, rgba(109,179,63,0.06) 60%, rgba(109,179,63,0.14) 100%);
  }
  .brand {
    position: absolute; display: flex; align-items: center; gap: 12px;
    color: var(--green); font-weight: 700; text-transform: uppercase;
  }
  .brand__dot {
    width: 34px; height: 34px; border-radius: 50%; background: var(--green); flex: none;
  }
  .brand__name { font-size: 26px; line-height: 1.05; letter-spacing: 0.5px; }
  .card--front .brand { left: 42px; top: 62px; }
  .card--back .brand { left: 50%; top: 104px; transform: translateX(-50%); }
  .contact { position: absolute; left: 51px; top: 198px; }
  .contact__name { color: var(--green); font-weight: 700; font-size: 17px; letter-spacing: 0.3px; }
  .contact__title { color: var(--grey); font-size: 13px; letter-spacing: 0.8px; margin-top: 3px; }
  .contact__lines { margin-top: 16px; color: var(--green); font-size: 14.5px; line-height: 20px; letter-spacing: 0.2px; }
  .message { position: absolute; left: 0; right: 0; top: 208px; text-align: center; }
  .message__rule { width: 14px; height: 2px; background: var(--green); margin: 0 auto 12px; }
  .message__text { color: var(--green); font-size: 15px; }
</style>
</head>
<body>
  <section class="card card--front">
    <div class="texture" role="img" aria-label="Dotted green particle texture sweeping along the right edge"></div>
    <div class="brand">
      <span class="brand__dot"></span>
      <span class="brand__name">Brixtender<br>Payments</span>
    </div>
    <div class="contact">
      <p class="contact__name">DANA MORVELL</p>
      <p class="contact__title">MANAGING DIRECTOR</p>
      <div class="contact__lines">
        <p>555-214-3980</p>
        <p>tmorvell@brixtender.example</p>
        <p>www.brixtender.example</p>
      </div>
    </div>
  </section>

  <section class="card card--back">
    <div class="texture" role="img" aria-label="Dotted green particle texture sweeping along the right edge"></div>
    <div class="brand">
      <span class="brand__dot"></span>
      <span class="brand__name">Brixtender<br>Payments</span>
    </div>
    <div class="message">
      <div class="message__rule"></div>
      <p class="message__text">No PCI Fees</p>
    </div>
  </section>
</body>
</html>
```